Email Signature and a letter head

I need a professional email signature and a letter head for letters sent by post. I've attached my logo and a signature i am currently using. Current letter head is also attached.

Target Market(s)

Accounting Clients

Industry/Entity Type

Public Accounting

Font styles to use
Sans Serif

Colors

Designer to choose colors to be used in the design.

Requirements
Must have
• My logo, PW Logo, Blumo Logo, Tax Agent logo. All attached.
• All my credentials - examples in the attached documents

```html
<!DOCTYPE html>
<html lang="en">
<head>
<meta charset="utf-8">
<title>Summit Ledger Letterhead</title>
<link href="https://fonts.googleapis.com/css2?family=Cinzel:wght@500&family=Jost:wght@400;500&family=Open+Sans:wght@400;600&display=swap" rel="stylesheet">
<style>
:root{
  --gold:#b8912f;
  --gold-light:#d9c28a;
  --ink:#1c1c1c;
  --grey:#6a6a6a;
  --bg:#d2d2d2;
  --paper:#ffffff;
  --badge-blue:#1aa6d8;
  --badge-teal:#127f91;
  --badge-green:#a7c83a;
}
*{margin:0;padding:0;box-sizing:border-box}
html,body{width:1200px;height:839px;overflow:hidden;background:var(--bg)}
.letterhead{position:absolute;left:314px;top:20px;width:572px;height:800px;background:var(--paper);box-shadow:8px 10px 14px rgba(0,0,0,.25);font-family:"Open Sans",Arial,sans-serif;color:var(--ink)}
.brand{position:absolute;left:0;top:62px;width:100%;display:flex;justify-content:center;align-items:center;gap:8px}
.brand-mark{width:22px;height:22px;border-radius:50%;background:var(--gold)}
.brand-name{font-family:"Jost",Arial,sans-serif;font-weight:500;color:var(--gold);font-size:20px;line-height:24px;letter-spacing:.5px}
.rule{position:absolute;height:1px;background:var(--gold)}
.contact{position:absolute;top:123px;display:flex;align-items:center;gap:5px;font-family:"Jost",Arial,sans-serif;font-size:7.5px;color:var(--grey)}
.contact svg{flex:none}
.contact.phone{top:120px;left:240px;font-size:12.5px;color:var(--gold);font-weight:500;letter-spacing:.5px}
.recipient{position:absolute;left:41px;top:181px;font-family:"Jost",Arial,sans-serif;font-size:9px;line-height:12px;letter-spacing:.6px;color:var(--grey);font-style:normal}
.recipient strong{color:var(--ink);font-weight:500}
.date{position:absolute;right:48px;top:181px;font-family:"Jost",Arial,sans-serif;font-size:9px;letter-spacing:.4px;color:#999}
.date strong{color:var(--ink);font-weight:500}
.body{position:absolute;left:41px;top:275px;width:483px;font-size:9.2px;line-height:12.3px;color:#333}
.body p{margin-bottom:12.3px}
.signature{position:absolute;left:41px;top:600px;width:114px;height:56px;background:linear-gradient(90deg,#f1f1f1,#e4e4e4);border-bottom:1.5px solid var(--ink)}
.footer-rule{position:absolute;left:36px;top:697px;width:500px;height:2px;background:linear-gradient(90deg,var(--gold-light),var(--gold) 40%,var(--gold) 60%,var(--gold-light))}
.holder{position:absolute;left:33px;top:715px;font-family:"Jost",Arial,sans-serif}
.holder-name{font-family:"Cinzel",Georgia,serif;font-weight:500;font-size:21px;line-height:24px;color:var(--ink)}
.holder-name small{font-family:"Jost",Arial,sans-serif;font-size:10px;font-weight:500}
.holder-ids{font-size:8.3px;color:#333;letter-spacing:.3px;margin-top:1px}
.holder-address{font-size:10px;font-weight:500;color:#222;margin-top:4px}
.partner{position:absolute;display:flex;align-items:center;gap:4px;font-family:"Jost",Arial,sans-serif;font-weight:500;font-size:10px}
.partner-dot{width:22px;height:22px;border-radius:50%;background:var(--badge-blue)}
.partner-blumo{left:300px;top:731px;color:var(--badge-teal)}
.partner-pw{left:390px;top:734px;color:var(--ink)}
.partner-pw .partner-square{width:14px;height:14px;background:#d6262d}
.tax-badge{position:absolute;left:465px;top:723px;width:38px;height:38px;border-radius:50%;background:var(--badge-green);border:3px solid #5a6b2a}
.tax-number{position:absolute;left:508px;top:731px;font-family:"Jost",Arial,sans-serif;font-size:6.5px;line-height:8px;color:var(--ink)}
</style>
</head>
<body>
<main class="letterhead">
  <header class="brand">
    <span class="brand-mark"></span>
    <span class="brand-name">Summit Ledger</span>
  </header>

  <div class="rule" style="left:18px;top:114px;width:201px"></div>
  <div class="rule" style="left:18px;top:143px;width:201px"></div>
  <div class="rule" style="left:351px;top:114px;width:202px"></div>
  <div class="rule" style="left:351px;top:143px;width:202px"></div>

  <div class="contact" style="left:20px">
    <svg width="13" height="13" viewBox="0 0 13 13"><circle cx="6.5" cy="6.5" r="6.5" fill="#222"/><rect x="3" y="4.2" width="7" height="4.6" rx=".6" fill="#fff"/><path d="M3 4.5l3.5 2.5 3.5-2.5" stroke="#222" stroke-width=".8" fill="none"/></svg>
    <span>corin@summitledgerservices.com.au</span>
  </div>
  <div class="contact phone">
    <svg width="18" height="18" viewBox="0 0 18 18"><circle cx="9" cy="9" r="9" fill="var(--gold)"/><path d="M5 7.5c0-1.5 8-1.5 8 0v1h-2v-1h-4v1H5z M6 9h6l1 3.5H5z" fill="#fff"/></svg>
    <span>0400 123 456</span>
  </div>
  <div class="contact" style="left:356px">
    <svg width="13" height="13" viewBox="0 0 13 13"><circle cx="6.5" cy="6.5" r="6.5" fill="#222"/><circle cx="6.5" cy="6.5" r="3.4" stroke="#fff" stroke-width="1" fill="none"/><path d="M3.1 6.5h6.8M6.5 3.1v6.8" stroke="#fff" stroke-width=".8"/></svg>
    <span>www.summitledgerservices.com.au</span>
  </div>

  <address class="recipient">
    <strong>To</strong><br>
    <strong>Owen Brooks,</strong><br>
    CEO, NORTHGATE STUDIO<br>
    M: +61 400 555 010
  </address>
  <div class="date"><strong>DATE:</strong> 17-01-2018</div>

  <section class="body">
    <p>Solum nullam principes vis no, eleifend postulant mediocrem ut est, ad tota partem quo. Vix lorem putant scribentur no, mea meis solet melius no, pri feugait noluisse appetere no. Ei mea graece suscipit, fastidii probatus est et. Duo ut oportere iudicabit, exerci laoreet vim id. An vidit quidam cum, ceteros phaedrum sit ea. Mollis incorrupte in vix. Noster mnesarchum vix ei.</p>
    <p>Lus te maluisset voluptatum quaerendum, no discere saperet persequeris cum, no pro nonumy partem phaedrum. Mel mazim corpora te. Has ad aeque mucius impetus, vel tation regione appetere ne. Porro voluptatum ius ut, ei docendi eloquentiam sea. Ne mandamus dignissim efficiendi eum, est id tota insolens, eu per facete latine.</p>
    <p>Sea te explicari conceptam definitionem, soluta constituto duo ad, usu an laudem latine voluptaria. Eam magna repudiare forensibus an. In nam euismod explicari voluptatibus. Petentium dissentiet ex eum, in eam ludus tantas aperiam. Eu est latine feugait suavitate.</p>
    <p>Eum ei augue voluptua copiosae. Vis cu altera noluisse intellegat. At vis probatus perpetua. Tale alterum interesset ne quo, est ad exerci oblique recusabo, eu sit simul legendos antiopam. Qui tacimates tractatos ad, delectus sapientem omittantur ut vis. Pro te graece equidem ancillae, indoctum molestiae eam ea.</p>
    <p>Sea te explicari conceptam definitionem, soluta constituto duo ad, usu an laudem latine voluptaria. Eam magna repudiare forensibus an. In nam euismod explicari voluptatibus. Petentium dissentiet ex eum, in eam ludus tantas aperiam. Eu est latine feugait suavitate.</p>
  </section>

  <div class="signature" role="img" aria-label="Handwritten signature of Corin Hale"></div>

  <div class="footer-rule"></div>
  <footer class="holder">
    <div class="holder-name">Corin Hale,<small>PW BBus</small></div>
    <div class="holder-ids">ABN: 12 345 678 901, TAN: 987 654 32</div>
    <div class="holder-address">18 Marlow Street, Hillcrest VIC 3000</div>
  </footer>

  <div class="partner partner-blumo"><span class="partner-dot"></span><span>Blumo</span></div>
  <div class="partner partner-pw"><span class="partner-square"></span><span>PW</span></div>
  <div class="tax-badge" role="img" aria-label="Registered tax agent badge"></div>
  <div class="tax-number">Tax agent<br>98765432</div>
</main>
</body>
</html>
```